Tech Startup Needs Business Card Design

I am looking for an eye catching business card design for our new company, Torn Kite. We are a place for business owners and contractors to share their experiences with their customers and check their current customers. Our website, www.torn-kite.co, may be able to offer some guidance as to the design.

Industry/Entity Type

Business

Contact Information for Business Card

Owen Barthwick
888-417-3083
Owen@torn-kite.co
www.torn-kite.co

```html
<!DOCTYPE html>
<html lang="en">
<head>
<meta charset="utf-8">
<title>Torn Kite — Business Card</title>
<link rel="stylesheet" href="https://fonts.googleapis.com/css2?family=Open+Sans:wght@400;600&display=swap">
<style>
  :root {
    --page: #e7e4df;
    --card: #ffffff;
    --card-shade: #ececec;
    --red: #e8262d;
    --ink: #1a1a1a;
    --grey-text: #444444;
    --rule: #c8c8c8;
    --circle-edge: #dcdcdc;
  }
  * { box-sizing: border-box; margin: 0; padding: 0; }
  html, body { width: 1200px; height: 843px; overflow: hidden; }
  body {
    background: var(--page);
    font-family: "Open Sans", Arial, sans-serif;
    position: relative;
  }
  .card {
    position: absolute;
    left: 280px;
    width: 640px;
    height: 366px;
    border-radius: 22px;
    background: linear-gradient(180deg, var(--card) 55%, var(--card-shade) 100%);
    overflow: hidden;
    box-shadow: 0 6px 18px rgba(0,0,0,0.18);
  }
  .card-back { top: 38px; }
  .card-front { top: 439px; }

  /* Back side */
  .scene-grid {
    position: absolute;
    left: 40px;
    top: 34px;
    display: grid;
    grid-template-columns: repeat(3, 140px);
    column-gap: 26px;
    row-gap: 14px;
  }
  .scene {
    display: flex;
    flex-direction: column;
    align-items: center;
  }
  .scene-art {
    width: 124px;
    height: 124px;
    border-radius: 50%;
    border: 2px solid var(--circle-edge);
  }
  .art-a { background: radial-gradient(circle at 50% 45%, #f1e3d3, #c7cfb0 70%, #eeeeee); }
  .art-b { background: radial-gradient(circle at 50% 50%, #e9e1d6, #b9a38c 65%, #eeeeee); }
  .art-c { background: radial-gradient(circle at 50% 55%, #dfe6da, #8fa08a 65%, #eeeeee); }
  .art-d { background: radial-gradient(circle at 50% 50%, #f0e4cf, #c98f6f 65%, #eeeeee); }
  .art-e { background: radial-gradient(circle at 50% 50%, #ece6de, #a9b3a0 65%, #eeeeee); }
  .art-f { background: radial-gradient(circle at 50% 50%, #efe3d5, #c67d6e 65%, #eeeeee); }
  .scene-label {
    margin-top: 8px;
    height: 20px;
    font-size: 15px;
    color: var(--grey-text);
  }
  .back-logo {
    position: absolute;
    right: 40px;
    top: 0;
    height: 366px;
    width: 70px;
    display: flex;
    align-items: center;
    justify-content: center;
  }
  .back-logo .wordmark {
    writing-mode: vertical-rl;
    transform: rotate(180deg);
    font-size: 50px;
  }

  /* Shared wordmark */
  .wordmark {
    display: flex;
    align-items: center;
    gap: 12px;
    white-space: nowrap;
    line-height: 1;
  }
  .wordmark-dot {
    width: 0.62em;
    height: 0.62em;
    border-radius: 50%;
    background: var(--red);
    flex: none;
  }
  .wordmark-name {
    font-weight: 600;
    color: var(--ink);
    letter-spacing: -0.5px;
  }
  .card-front .wordmark {
    position: absolute;
    left: 50%;
    top: 78px;
    transform: translateX(-50%);
    font-size: 64px;
  }

  /* Front side */
  .identity {
    position: absolute;
    left: 100px;
    top: 190px;
    width: 212px;
    text-align: right;
  }
  .person-name {
    font-size: 25px;
    color: var(--red);
    white-space: nowrap;
  }
  .person-title {
    font-size: 19px;
    color: var(--ink);
    margin-top: 2px;
  }
  .divider {
    position: absolute;
    left: 328px;
    top: 188px;
    width: 1px;
    height: 84px;
    background: var(--rule);
  }
  .contacts {
    position: absolute;
    left: 346px;
    top: 186px;
    list-style: none;
  }
  .contacts li {
    display: flex;
    align-items: center;
    gap: 10px;
    font-size: 18px;
    color: var(--grey-text);
    line-height: 28px;
    white-space: nowrap;
  }
  .contacts svg { width: 16px; height: 16px; flex: none; }
  .front-band {
    position: absolute;
    left: 0;
    bottom: 0;
    width: 640px;
    height: 34px;
  }
</style>
</head>
<body>

  <section class="card card-back" aria-label="Card back">
    <div class="scene-grid">
      <figure class="scene">
        <div class="scene-art art-a" role="img" aria-label="Illustration of two contractors standing together"></div>
        <figcaption class="scene-label">Contactors</figcaption>
      </figure>
      <figure class="scene">
        <div class="scene-art art-b" role="img" aria-label="Illustration of an awkward moment between a homeowner and a worker at a fence"></div>
        <figcaption class="scene-label">Awkward</figcaption>
      </figure>
      <figure class="scene">
        <div class="scene-art art-c" role="img" aria-label="Illustration of a man on a sofa thinking about money"></div>
        <figcaption class="scene-label">Thinking</figcaption>
      </figure>
      <figure class="scene">
        <div class="scene-art art-d" role="img" aria-label="Illustration of a worker running off with a bag of money"></div>
        <figcaption class="scene-label">Steeling-Money</figcaption>
      </figure>
      <figure class="scene">
        <div class="scene-art art-e" role="img" aria-label="Illustration of a contractor and a customer talking"></div>
        <figcaption class="scene-label"></figcaption>
      </figure>
      <figure class="scene">
        <div class="scene-art art-f" role="img" aria-label="Illustration of a contractor and a customer posing together"></div>
        <figcaption class="scene-label"></figcaption>
      </figure>
    </div>
    <div class="back-logo">
      <div class="wordmark">
        <span class="wordmark-dot"></span>
        <span class="wordmark-name">Torn Kite</span>
      </div>
    </div>
  </section>

  <section class="card card-front" aria-label="Card front">
    <div class="wordmark">
      <span class="wordmark-dot"></span>
      <span class="wordmark-name">Torn Kite</span>
    </div>

    <div class="identity">
      <p class="person-name">Owen Barthwick</p>
      <p class="person-title">CEO/Founder</p>
    </div>
    <div class="divider"></div>

    <ul class="contacts">
      <li>
        <svg viewBox="0 0 16 16" aria-hidden="true"><path fill="#e8262d" d="M3.6 1.2l2.2 2.6-1.2 1.7c.9 2 2.2 3.4 4.2 4.3l1.7-1.2 2.6 2.2-1.3 2.5C7 13.1 2.9 9 1.1 3.3z"/></svg>
        <span>888-417-3083</span>
      </li>
      <li>
        <svg viewBox="0 0 16 16" aria-hidden="true"><rect x="1" y="3" width="14" height="10" rx="1.5" fill="#e8262d"/><path d="M1.5 3.8L8 9l6.5-5.2" stroke="#fff" stroke-width="1.3" fill="none"/></svg>
        <span>Owen@torn-kite.co</span>
      </li>
      <li>
        <svg viewBox="0 0 16 16" aria-hidden="true"><circle cx="8" cy="8" r="7" fill="#e8262d"/><path d="M1 8h14M8 1c-3 3.5-3 10.5 0 14M8 1c3 3.5 3 10.5 0 14" stroke="#fff" stroke-width="1" fill="none"/></svg>
        <span>www.torn-kite.co</span>
      </li>
    </ul>

    <svg class="front-band" viewBox="0 0 640 34" preserveAspectRatio="none" aria-hidden="true">
      <defs>
        <linearGradient id="bandRed" x1="0" y1="0" x2="0" y2="1">
          <stop offset="0" stop-color="#f0353b"/>
          <stop offset="1" stop-color="#b9141a"/>
        </linearGradient>
        <linearGradient id="bandBlack" x1="0" y1="0" x2="0" y2="1">
          <stop offset="0" stop-color="#2a2a2a"/>
          <stop offset="1" stop-color="#050505"/>
        </linearGradient>
      </defs>
      <rect x="0" y="0" width="640" height="34" fill="url(#bandBlack)"/>
      <path d="M0 0H430L412 34H0Z" fill="url(#bandRed)"/>
    </svg>
  </section>

</body>
</html>
```